New Wordpress Design Project: TR- Tamberly Roots, Training Beyond Equity, Diversity, and Inclusion

I need a clean, modern, website design for TR- a national consulting firm providing equity, diversity, and inclusion training, through the lens of undoing racism, for arts and culture, and the non profit industry. It will feature both written posts, and some video. People will need TR contact information, and subscribe to receive information. It will feature a pretty active blog, and a section for resources, with links to other sites. There needs to be a section about TR,its training, approach, and bio Information. I probably should have put this first!

I want a site that draws people in. That is interesting and dynamic. My approach to this work is to provide people with the information, knowledge, and tools they need to go back to their communities and do the work. So they are at the center of the story. And I like powerful imagery. It could also be pretty.

The idea of undoing racism is a big idea. It is powerful, heroic even. And thousands of people in the US are working hard to do just that. So there is a sense of movement building here, of connecting to something important.

I already have a logo design that was done through a contest here last month.

Target Market(s)

Arts and culture fields, non profit industry, and philanthropy

Font styles to use
Sans Serif

Requirements
Must have
• Must have dynamic powerful imagery, be clean and easy to navigate, support concept of story telling, good use of color, be inviting, draw people in to learn when they see it first time. The ability to update photos, and videos easily. Connect to social media, especially Pinglomar and Tallyhive.
Nice to have
• It would be nice to have a website that uses more images than words to tell stories. I don't know enough about what's possible in website design to add more to this section.
Should not have
• Should not look like we are selling products, or services even but, rather, providing essential information and knowledge to help people make this world a better place for more people.

```html
<!DOCTYPE html>
<html lang="en">
<head>
<meta charset="utf-8">
<title>Tamberly Roots – Home</title>
<link href="https://fonts.googleapis.com/css2?family=Lato:wght@400;700;900&family=Federo&family=Exo+2:wght@700&display=swap" rel="stylesheet">
<style>
:root{
  --yellow:#ffdd00;
  --yellow-deep:#f5c900;
  --black:#0b0b0b;
  --charcoal:#333333;
  --charcoal-dark:#262626;
  --light:#f2f2f2;
  --text:#222222;
  --muted:#555555;
  --white:#ffffff;
}
*{box-sizing:border-box;margin:0;padding:0}
html,body{width:1200px;height:2281px;overflow:hidden;background:var(--white)}
body{font-family:"Lato",sans-serif;color:var(--text)}
.page{position:relative;width:1200px;height:2281px;overflow:hidden}
.abs{position:absolute}
.display{font-family:"Federo",sans-serif;font-weight:400}

/* header */
.topbar{position:absolute;left:0;top:0;width:1200px;height:99px;background:var(--black)}
.contact-chip{position:absolute;top:26px;display:flex;gap:14px;color:var(--white);font-size:15px;line-height:20px}
.contact-chip strong{font-weight:700;display:block}
.contact-chip svg{flex:none}
.navbar{position:absolute;left:0;top:99px;width:1200px;height:41px;background:var(--yellow)}
.nav-item{position:absolute;top:0;height:41px;line-height:41px;font-size:16px;color:var(--text);text-align:center;width:120px;margin-left:-60px}
.nav-item.active{font-weight:700}
.nav-sep{position:absolute;top:6px;width:1px;height:30px;background:#d9b800}
.brand-tab{position:absolute;left:502px;top:0;width:196px;height:140px}
.brand-name{position:absolute;left:0;width:1200px;text-align:center;color:var(--white);font-family:"Lato",sans-serif;font-weight:700}

/* hero */
.hero{position:absolute;left:0;top:140px;width:1200px;height:526px;background:linear-gradient(160deg,#8a7357 0%,#b29a78 40%,#9c8362 70%,#6f5a42 100%)}
.hero-caption{position:absolute;left:198px;top:380px;width:805px;height:88px;background:rgba(40,30,20,.55);color:var(--white);font-family:"Exo 2",sans-serif;font-weight:700;font-size:27px;line-height:34px;text-align:center;padding-top:10px;letter-spacing:.5px}
.dots{position:absolute;top:484px;left:564px;display:flex;gap:10px}
.dot{width:14px;height:14px;border-radius:50%;background:var(--white);border:2px solid var(--charcoal)}
.dot.on{background:var(--yellow)}

/* features */
.features{position:absolute;left:0;top:666px;width:1200px;height:180px}
.feature{position:absolute;top:0;width:480px;text-align:center}
.feature-icon{position:absolute;top:-36px;left:204px;width:72px;height:72px;border-radius:50%;display:flex;align-items:center;justify-content:center}
.feature h3{margin-top:53px;font-family:"Federo",sans-serif;font-weight:400;font-size:25px}
.feature p{margin:10px auto 0;width:360px;font-size:13px;line-height:20px}
.feature .plus{margin:12px auto 0;width:26px;height:24px;border-radius:3px;font-weight:900;font-size:18px;line-height:24px}
.feature.training{left:43px;color:var(--white)}
.feature.training .feature-icon{background:var(--yellow)}
.feature.training .plus{background:var(--yellow);color:var(--black)}
.feature.approach{left:640px;color:var(--black)}
.feature.approach .feature-icon{background:var(--charcoal)}
.feature.approach .plus{background:var(--charcoal);color:var(--white)}

/* welcome */
.welcome{position:absolute;left:0;top:846px;width:1200px;height:365px;background:var(--light)}
.section-title{font-family:"Federo",sans-serif;font-size:29px;color:var(--black)}
.rule{position:absolute;height:2px;background:var(--charcoal)}
.welcome .lead{position:absolute;left:100px;top:116px;width:660px;font-weight:700;font-size:17px;line-height:26px;color:var(--black)}
.welcome .body{position:absolute;left:100px;top:178px;width:660px;font-size:13px;line-height:21px;color:var(--text)}
.pill{position:absolute;border-radius:20px;font-weight:700;text-align:center}
.video{position:absolute;left:802px;top:88px;width:301px;height:222px;border:1px solid #999;border-radius:3px;overflow:hidden;box-shadow:0 6px 10px rgba(0,0,0,.2)}
.video-frame{position:absolute;left:0;top:0;width:301px;height:192px;background:linear-gradient(120deg,#dfe6ea 0%,#c7ccd1 40%,#5a6675 75%,#2c3440 100%)}
.video-bar{position:absolute;left:0;top:192px;width:301px;height:30px;background:linear-gradient(#3a3a3a,#151515)}

/* objective */
.objective{position:absolute;left:0;top:1211px;width:1200px;height:219px;background:var(--yellow)}
.objective h2{position:absolute;left:0;top:36px;width:1200px;text-align:center;font-family:"Federo",sans-serif;font-weight:400;font-size:28px;line-height:43px;color:var(--black)}

/* inquiry */
.inquiry{position:absolute;left:0;top:1430px;width:1200px;height:193px;background:repeating-linear-gradient(45deg,#141414 0 2px,#0c0c0c 2px 4px)}
.inquiry h2{position:absolute;left:0;top:32px;width:1200px;text-align:center;font-family:"Federo",sans-serif;font-weight:400;font-size:29px;color:var(--white)}
.field{position:absolute;top:100px;height:47px;background:var(--white);border-radius:2px;font-size:14px;padding:14px 12px;color:#444}
.submit{position:absolute;left:922px;top:100px;width:181px;height:47px;background:var(--yellow);border:1px solid #c9a800;font-family:"Federo",sans-serif;font-size:20px;line-height:45px;text-align:center;color:var(--black)}

/* blog */
.blog{position:absolute;left:0;top:1623px;width:1200px;height:377px;background:var(--white)}
.blog .section-title{font-size:28px}
.pager{position:absolute;font-size:20px;color:#999;letter-spacing:6px}
.pager b{color:var(--black);font-weight:400}
.post{position:absolute;left:100px;width:470px;height:92px}
.post .thumb{position:absolute;left:0;top:0;width:115px;height:91px;border:1px solid #ddd}
.post h4{position:absolute;left:146px;top:6px;font-size:15px;font-weight:700;color:var(--black)}
.post p{position:absolute;left:146px;top:30px;width:310px;font-size:12.5px;line-height:20px;color:var(--text)}
.post .meta{position:absolute;left:146px;top:76px;font-size:12.5px;display:flex;gap:30px;align-items:center}
.meta span{display:flex;gap:8px;align-items:center}
.recent{position:absolute;left:646px;width:460px;display:flex;gap:16px;font-size:12.5px;line-height:18px}

/* footer */
.footer{position:absolute;left:0;top:2000px;width:1200px;height:236px;background:var(--charcoal)}
.footer h5{position:absolute;top:40px;font-size:15px;font-weight:700;color:var(--white)}
.footer .underline{position:absolute;top:64px;height:1px;background:#777}
.footer .underline i{position:absolute;left:0;top:0;width:40px;height:1px;background:var(--yellow)}
.quick-links{position:absolute;left:100px;top:76px;list-style:none;font-size:13px;line-height:23.5px;color:var(--white)}
.quick-links li::before{content:"→";color:var(--yellow);margin-right:12px}
.quick-links li.active{color:var(--yellow)}
.footer .col-sep{position:absolute;top:36px;width:1px;height:170px;background:#4a4a4a}
.contact-detail{position:absolute;left:306px;top:80px;font-size:12.5px;line-height:18px;color:var(--white)}
.contact-line{display:flex;gap:12px;align-items:center;margin-top:8px}
.newsletter{position:absolute;left:585px;top:78px;width:190px;font-size:12px;line-height:17px;color:var(--white)}
.email-box{margin-top:16px;width:190px;height:26px;background:var(--white);border-radius:3px;color:var(--black);font-size:11px;font-weight:700;padding:6px 6px}
.subscribe{margin-top:10px;width:104px;height:26px;background:var(--yellow);border-radius:2px;color:var(--black);font-size:13px;font-weight:700;text-align:center;line-height:26px}
.copyright{position:absolute;left:0;top:2236px;width:1200px;height:45px;background:#1c1c1c;color:var(--white);font-size:12.5px;text-align:center;line-height:45px}
</style>
</head>
<body>
<div class="page">

  <!-- header -->
  <header class="topbar">
    <div class="contact-chip" style="left:100px">
      <svg width="34" height="34" viewBox="0 0 34 34"><circle cx="17" cy="17" r="15" fill="none" stroke="#ffdd00" stroke-width="2.5"/><path d="M11 9c-2 2-1 7 3 11s9 5 11 3l-3-4-3 2c-2-1-4-3-5-5l2-3z" fill="#ffdd00"/></svg>
      <div><strong>Call Us:</strong>123 456 7890</div>
    </div>
    <div class="contact-chip" style="left:858px">
      <svg width="36" height="32" viewBox="0 0 36 32"><rect x="3" y="6" width="28" height="20" fill="none" stroke="#ffdd00" stroke-width="2.5" transform="rotate(-10 17 16)"/><path d="M4 9l14 10 14-12" fill="none" stroke="#ffdd00" stroke-width="2.5"/></svg>
      <div><strong>Mail Us:</strong>inquiry@tamberlyroots.com</div>
    </div>
  </header>

  <nav class="navbar">
    <div class="nav-item active" style="left:155px">Home</div>
    <div class="nav-sep" style="left:214px"></div>
    <div class="nav-item" style="left:274px">About Us</div>
    <div class="nav-sep" style="left:334px"></div>
    <div class="nav-item" style="left:398px">Services</div>
    <div class="nav-item" style="left:791px">Blog Posts</div>
    <div class="nav-sep" style="left:864px"></div>
    <div class="nav-item" style="left:925px">Gallery</div>
    <div class="nav-sep" style="left:987px"></div>
    <div class="nav-item" style="left:1060px">Contact Us</div>
  </nav>

  <svg class="abs" style="left:490px;top:0" width="220" height="142" viewBox="0 0 220 142" aria-hidden="true">
    <path d="M0 99 Q14 99 18 112 L22 126 Q27 140 42 140 L178 140 Q193 140 198 126 L202 112 Q206 99 220 99 L220 0 L0 0Z" fill="#0b0b0b"/>
  </svg>
  <div class="abs" style="left:583px;top:22px;width:34px;height:34px;border-radius:50%;background:var(--yellow)"></div>
  <div class="brand-name" style="top:72px;font-size:22px">Tamberly Roots</div>

  <!-- hero -->
  <section class="hero" role="img" aria-label="Hands of many people meeting in a circle on sand">
    <div class="hero-caption">WE ARE AN INSURANCE AGENCY SPECIALIZING IN PRICING<br>CONSULTANCY</div>
    <div class="dots"><span class="dot"></span><span class="dot on"></span><span class="dot"></span></div>
  </section>

  <!-- features -->
  <section class="features">
    <svg class="abs" style="left:0;top:0" width="1200" height="180" viewBox="0 0 1200 180" aria-hidden="true">
      <rect width="1200" height="180" fill="#ffdd00"/>
      <polygon points="0,0 616,0 556,180 0,180" fill="#333333"/>
      <polygon points="616,0 628,0 568,180 556,180" fill="#ffffff"/>
    </svg>
    <div class="abs" style="left:535px;top:45px;width:116px;height:116px;border-radius:50%;background:var(--yellow);border:6px solid var(--white)"></div>

    <div class="feature training">
      <div class="feature-icon">
        <svg width="38" height="38" viewBox="0 0 38 38"><rect x="14" y="3" width="20" height="14" fill="none" stroke="#0b0b0b" stroke-width="2.5"/><circle cx="9" cy="16" r="4" fill="#0b0b0b"/><circle cx="19" cy="26" r="4" fill="#0b0b0b"/><circle cx="30" cy="26" r="4" fill="#0b0b0b"/><path d="M2 36c0-6 3-9 7-9s7 3 7 9zM13 38c0-4 3-6 6-6s6 2 6 6zM24 38c0-4 3-6 6-6s6 2 6 6z" fill="#0b0b0b"/></svg>
      </div>
      <h3>Training</h3>
      <p>Lorem ipsum dolor sit amet, consectetuer adipiscing elit, sed diam nonummy nibh euismod tincidunt ut laoreet</p>
      <div class="plus">+</div>
    </div>
    <div class="feature approach">
      <div class="feature-icon">
        <svg width="36" height="36" viewBox="0 0 36 36"><path d="M18 34V18M18 18L8 8M18 18L28 8" fill="none" stroke="#ffdd00" stroke-width="4"/><path d="M4 4h9L4 13zM32 4h-9l9 9z" fill="#ffdd00"/></svg>
      </div>
      <h3>Approach</h3>
      <p>Lorem ipsum dolor sit amet, consectetuer adipiscing elit, sed diam nonummy nibh euismod tincidunt ut laoreet</p>
      <div class="plus">+</div>
    </div>
  </section>

  <!-- welcome -->
  <section class="welcome">
    <h2 class="section-title abs" style="left:100px;top:50px">Welcome To Tamberly Roots</h2>
    <div class="rule" style="left:100px;top:99px;width:645px"></div>
    <p class="lead">Lorem ipsum dolor sit amet, consectetuer adipiscing elit, sed diam nonummy nibh euismod tincidunt ut laoreet dolore magna aliquam erat volutpat.</p>
    <p class="body">Lorem ipsum dolor sit amet, consectetuer adipiscing elit, sed diam nonummy nibh euismod tincidunt uterr laoreet dolore magna aliquam erat volutpat. Ut wisi enim ad minim veniam, quis nostrud exerci tationerwi laoreet dolore magna aliquam erati volutpat. Ut wisi enim ad minim veniam, quis nostrud exerci iationweri ullamcorpererer suscipit lobortis nisl uterr aliquip ex ea commodo consequat.</p>
    <div class="pill" style="left:100px;top:280px;width:128px;height:38px;line-height:38px;background:var(--yellow);font-size:15px;color:var(--black)">Read More</div>
    <div class="video">
      <div class="video-frame" role="img" aria-label="Video still of a team meeting with a handshake across a table"></div>
      <svg class="abs" style="left:128px;top:78px" width="46" height="34" viewBox="0 0 46 34" aria-hidden="true"><rect width="46" height="34" rx="8" fill="#111"/><path d="M18 10l12 7-12 7z" fill="#fff"/></svg>
      <div class="video-bar">
        <svg width="301" height="30" viewBox="0 0 301 30" aria-hidden="true"><path d="M14 12h4l5-4v14l-5-4h-4z" fill="#ddd"/><rect x="40" y="13" width="230" height="4" rx="2" fill="#555"/><rect x="40" y="13" width="75" height="4" rx="2" fill="#d91e18"/><path d="M282 9h6v6M288 9l-7 7M281 21h-6v-6" fill="none" stroke="#ddd" stroke-width="2"/></svg>
      </div>
    </div>
  </section>

  <!-- objective -->
  <section class="objective">
    <h2>Our Objective Is To Maintain A Culture of Mutual Respect And Consideration,<br>Ensuring That Everyone Is Treated Equally</h2>
    <div class="pill" style="left:508px;top:144px;width:132px;height:38px;line-height:38px;background:var(--black);color:var(--white);font-size:16px">Get Started</div>
  </section>

  <!-- quick inquiry -->
  <section class="inquiry">
    <h2>Quick Inquiry</h2>
    <div class="field" style="left:100px;width:223px">Name</div>
    <div class="field" style="left:347px;width:222px">Email</div>
    <div class="field" style="left:593px;width:305px">Message</div>
    <div class="submit">Get Started</div>
  </section>

  <!-- blog -->
  <section class="blog">
    <svg class="abs" style="left:100px;top:42px" width="34" height="28" viewBox="0 0 34 28" aria-hidden="true"><ellipse cx="14" cy="11" rx="14" ry="10" fill="#f5c900"/><path d="M6 18l-3 8 9-6z" fill="#f5c900"/><ellipse cx="22" cy="15" rx="10" ry="7" fill="#ffdd00"/></svg>
    <h2 class="section-title abs" style="left:146px;top:36px">Latest Blog</h2>
    <div class="rule" style="left:100px;top:88px;width:505px;height:1px;background:#888"></div>
    <div class="rule" style="left:100px;top:87px;width:80px;height:3px;background:var(--yellow)"></div>
    <div class="pager" style="left:536px;top:44px">‹<b>›</b></div>

    <article class="post" style="top:111px">
      <div class="thumb" role="img" aria-label="Hands reviewing a printed bar chart" style="background:linear-gradient(135deg,#e8eef5,#9cb5d6 60%,#3e6db0)"></div>
      <h4>Ut wisi enim ad minim veniam, quiswerer</h4>
      <p>Lorem ipsum dolor sit amet, consectetuer adipcing elit, sed diam nonummy nibh &nbsp;...[+]</p>
      <div class="meta">
        <span><svg width="12" height="12" viewBox="0 0 12 12"><circle cx="6" cy="6" r="5" fill="none" stroke="#f5c900" stroke-width="1.6"/><path d="M6 3v3h2" fill="none" stroke="#f5c900" stroke-width="1.4"/></svg>3:50 Pm</span>
        <span><svg width="12" height="12" viewBox="0 0 12 12"><rect x="1" y="2" width="10" height="9" fill="none" stroke="#f5c900" stroke-width="1.5"/><path d="M1 5h10" stroke="#f5c900" stroke-width="1.5"/></svg>Dec 10, 2016</span>
      </div>
    </article>
    <article class="post" style="top:233px">
      <div class="thumb" role="img" aria-label="Business colleagues shaking hands in an office" style="background:linear-gradient(135deg,#dfe3e8,#8c96a3 55%,#2f3a4a)"></div>
      <h4>Ut wisi enim ad minim veniam, quiswerer</h4>
      <p>Lorem ipsum dolor sit amet, consectetuer adipcing elit, sed diam nonummy nibh &nbsp;...[+]</p>
      <div class="meta">
        <span><svg width="12" height="12" viewBox="0 0 12 12"><circle cx="6" cy="6" r="5" fill="none" stroke="#f5c900" stroke-width="1.6"/><path d="M6 3v3h2" fill="none" stroke="#f5c900" stroke-width="1.4"/></svg>3:50 Pm</span>
        <span><svg width="12" height="12" viewBox="0 0 12 12"><rect x="1" y="2" width="10" height="9" fill="none" stroke="#f5c900" stroke-width="1.5"/><path d="M1 5h10" stroke="#f5c900" stroke-width="1.5"/></svg>Dec 10, 2016</span>
      </div>
    </article>

    <svg class="abs" style="left:646px;top:44px" width="28" height="26" viewBox="0 0 28 26" aria-hidden="true"><rect x="1" y="9" width="24" height="16" fill="#111"/><path d="M1 9l12 9 12-9" fill="none" stroke="#fff" stroke-width="1.6"/><path d="M6 2l6 3-2 2z" fill="#f5c900"/></svg>
    <h2 class="section-title abs" style="left:686px;top:38px">Recent Posts</h2>
    <div class="rule" style="left:646px;top:88px;width:458px;height:1px;background:#888"></div>
    <div class="rule" style="left:646px;top:87px;width:115px;height:3px;background:var(--yellow)"></div>
    <div class="pager" style="left:1076px;top:44px">‹<b>›</b></div>

    <div class="recent" style="top:104px"><svg width="26" height="26" viewBox="0 0 26 26" style="flex:none;margin-top:6px"><path d="M4 22l2-7L19 2l5 5L11 20z" fill="none" stroke="#111" stroke-width="2"/><path d="M4 22l2-7 5 5z" fill="#111"/></svg><span>Lorem ipsum dolor sit amet, consectetuer adipiscing elit, sed diam no nummy nibh euismod tincidunt uterr laoreet dolore</span></div>
    <div class="recent" style="top:161px"><svg width="26" height="26" viewBox="0 0 26 26" style="flex:none;margin-top:6px"><path d="M4 22l2-7L19 2l5 5L11 20z" fill="none" stroke="#111" stroke-width="2"/><path d="M4 22l2-7 5 5z" fill="#111"/></svg><span>Lorem ipsum dolor sit amet, consectetuer adipiscing elit, sed diam no nummy nibh euismod tincidunt uterr laoreet dolore</span></div>
    <div class="recent" style="top:219px"><svg width="26" height="26" viewBox="0 0 26 26" style="flex:none;margin-top:6px"><path d="M4 22l2-7L19 2l5 5L11 20z" fill="none" stroke="#111" stroke-width="2"/><path d="M4 22l2-7 5 5z" fill="#111"/></svg><span>Lorem ipsum dolor sit amet, consectetuer adipiscing elit, sed diam no nummy nibh euismod tincidunt uterr laoreet dolore</span></div>
    <div class="recent" style="top:276px"><svg width="26" height="26" viewBox="0 0 26 26" style="flex:none;margin-top:6px"><path d="M4 22l2-7L19 2l5 5L11 20z" fill="none" stroke="#111" stroke-width="2"/><path d="M4 22l2-7 5 5z" fill="#111"/></svg><span>Lorem ipsum dolor sit amet, consectetuer adipiscing elit, sed diam no nummy nibh euismod tincidunt uterr laoreet dolore</span></div>
  </section>

  <!-- footer -->
  <footer class="footer">
    <h5 style="left:100px">Quick Links</h5>
    <div class="underline" style="left:100px;width:100px"><i></i></div>
    <ul class="quick-links">
      <li class="active">Home</li><li>About Us</li><li>Services</li><li>Blog Posts</li><li>Gallery</li><li>Contact Us</li>
    </ul>
    <div class="col-sep" style="left:274px"></div>

    <h5 style="left:306px">Contact Detail</h5>
    <div class="underline" style="left:306px;width:175px"><i></i></div>
    <div class="contact-detail">
      <strong>TR Firm</strong><br>16 Lorem ipsum dolor sit amet<br>sed benetion, Street no-123456
      <div class="contact-line" style="margin-top:12px"><svg width="12" height="12" viewBox="0 0 12 12"><path d="M2 1c-2 2 0 6 3 8s5 3 6 1l-2-3-2 1c-1-1-2-2-2-3l1-2z" fill="#ffdd00"/></svg>123-456-1789</div>
      <div class="contact-line"><svg width="12" height="12" viewBox="0 0 12 12"><rect x="1" y="5" width="10" height="6" fill="#ffdd00"/><rect x="3" y="1" width="6" height="4" fill="none" stroke="#ffdd00" stroke-width="1.4"/></svg>123-456-1789</div>
      <div class="contact-line"><svg width="12" height="10" viewBox="0 0 12 10"><rect x="0" y="0" width="12" height="10" fill="#ffdd00"/><path d="M0 0l6 5 6-5" fill="none" stroke="#333" stroke-width="1.2"/></svg>inquiry@trfirm.com</div>
    </div>
    <div class="col-sep" style="left:532px"></div>

    <h5 style="left:585px">Newsletter Signup</h5>
    <div class="underline" style="left:585px;width:190px"><i></i></div>
    <div class="newsletter">
      Get latest updates by entering your email address
      <div class="email-box">Email Address</div>
      <div class="subscribe">SUBSCRIBE</div>
    </div>
    <div class="col-sep" style="left:829px"></div>

    <div class="abs" style="left:974px;top:68px;width:38px;height:38px;border-radius:50%;background:var(--yellow)"></div>
    <div class="abs" style="left:860px;top:118px;width:290px;text-align:center;color:var(--white);font-weight:700;font-size:26px">Tamberly Roots</div>
  </footer>
  <div class="copyright">Copyright © 2017 Trfirm. All Rights Reserved.</div>
</div>
</body>
</html>
```